Web design for Restwell Sleep Clinic

We´re a group of Phisicians and working with patients with snoring e sleep apnea problems.
We´re beginning to offer home sleep studies (an option to lab studies) and we ´re building a webpage to share information, to find patients and to offer our product.
We already have a www adress and some idea about logo and brand.
We´re in Brazil and our service/webpage will be in Portuguese.

```html
<!DOCTYPE html>
<html lang="en">
<head>
<meta charset="utf-8">
<title>Restwell Sleep Clinic</title>
<link href="https://fonts.googleapis.com/css2?family=Open+Sans:ital,wght@0,400;0,600;1,400&family=Yanone+Kaffeesatz:wght@300;400&display=swap" rel="stylesheet">
<style>
:root{
  --blue:#2f7fc7;
  --blue-light:#5ba0d8;
  --blue-sky:#8cc8f0;
  --red:#ed1c24;
  --grey-text:#666;
  --grey-line:#e2e2e2;
  --row-bg:#eeeeee;
  --footer-bg:#e6e6e8;
  --page-bg:#fafafa;
}
*{box-sizing:border-box;margin:0;padding:0}
html,body{width:960px;height:1200px;overflow:hidden;background:#fff}
body{font-family:"Open Sans",sans-serif;color:var(--grey-text);position:relative}
.page{position:absolute;left:53px;top:16px;width:792px;height:1158px;background:linear-gradient(#f2f2f2,#fff 160px);}
.abs{position:absolute}
.display{font-family:"Yanone Kaffeesatz",sans-serif;font-weight:400;color:var(--blue)}
.brand{left:53px;top:58px;display:flex;align-items:center;gap:6px}
.brand-mark{width:22px;height:22px;border-radius:50%;background:var(--blue)}
.brand-name{font-family:"Yanone Kaffeesatz",sans-serif;font-size:24px;color:var(--blue);line-height:1}
.social{left:621px;top:22px;display:flex;gap:7px}
.social span{width:17px;height:17px;background:#b5b5b5;display:block}
.contact-top{right:54px;top:48px;text-align:right;font-size:8.5px;line-height:13px;color:#555}
.contact-top a{color:var(--blue)}
.search{left:597px;top:106px;width:140px;height:17px;background:#fff;font-size:7.5px;color:#999;padding:3px 8px;border:1px solid #eee}
.search-btn{left:711px;top:106px;width:26px;height:17px;background:var(--blue)}
.nav{left:49px;top:117px;width:696px;height:33px;background:var(--red);display:flex;align-items:center;padding-left:7px;gap:15px}
.nav a{color:#fff;font-size:8.5px;text-decoration:none;letter-spacing:.2px}
.hero-deco{left:0;top:150px}
.hero{left:49px;top:150px;width:696px;height:240px;background:radial-gradient(circle at 45% 40%,#d4ecfb,var(--blue-sky) 40%,#3d97d8 100%);clip-path:polygon(0 0,100% 0,100% 92%,60% 96%,19% 100%,0 82%)}
.hero-photo{right:0;top:0;width:220px;height:225px;background:linear-gradient(160deg,#f3d2bd,#e8e8ee 55%,#cfd8e2)}
.hero-panel{left:76px;top:204px;width:357px;height:148px;background:rgba(76,150,210,.92);padding:18px 0 0 63px;color:#fff}
.hero-panel h1{font-weight:400;font-size:24px;letter-spacing:.5px;margin-bottom:10px}
.hero-panel p{font-size:8.5px;line-height:12.5px;width:250px;margin-left:22px}
.hero-panel .more{font-family:"Yanone Kaffeesatz",sans-serif;font-size:16px;margin:12px 0 0 51px;display:flex;align-items:center;gap:5px}
.more i{width:17px;height:17px;border-radius:50%;background:#fff;display:inline-block;position:relative}
.more i:after{content:"";position:absolute;left:5px;top:4px;border:5px solid transparent;border-left:7px solid var(--blue-light);border-right:0}
.dots{left:702px;top:379px;display:flex;gap:3px}
.dots span{width:8px;height:7px;background:#ccc}
.dots span:first-child{background:var(--blue)}
.tab{left:0;top:159px;width:20px;height:70px;background:#333;color:#fff;font-size:7px;writing-mode:vertical-rl;display:flex;align-items:center;justify-content:center}
.intro{left:49px;top:432px;font-size:24px}
.cards{left:49px;top:468px;display:flex;gap:14px}
.card{width:164px;height:183px;border:1px solid var(--grey-line);background:#fff;text-align:center;padding-top:12px}
.card .ico{width:45px;height:45px;border-radius:50%;background:var(--blue);margin:0 auto;display:flex;align-items:center;justify-content:center}
.card h2{font-family:"Yanone Kaffeesatz",sans-serif;font-weight:400;color:var(--blue);font-size:20px;margin:10px 0 8px}
.card p{font-size:8.7px;line-height:14px;padding:0 12px}
.doctors-title{left:49px;top:668px;font-size:19px}
.rule{left:49px;top:700px;width:696px;height:4px;background:#f2f2f2}
.rule:before{content:"";position:absolute;left:0;top:0;width:26px;height:4px;background:var(--blue)}
.doctors{left:49px;top:721px;display:flex;gap:14px}
.doc{width:164px;height:151px;border:1px solid var(--grey-line);padding:4px;background:#fff}
.doc div{width:100%;height:100%}
.appt-title{left:49px;top:894px;font-size:19px}
.appt-rule{left:49px;top:927px;width:214px;height:4px;background:#f2f2f2}
.appt-rule:before{content:"";position:absolute;left:0;width:26px;height:4px;background:var(--blue)}
.appt-text{left:49px;top:950px;width:222px;font-style:italic;font-size:8.5px;line-height:14px;color:#555}
.appt-line{left:53px;font-size:8.5px;color:#333;display:flex;align-items:center;gap:12px}
.appt-line a{color:#333}
.btn{left:49px;top:1073px;width:80px;height:25px;background:var(--red);color:#fff;font-family:"Yanone Kaffeesatz",sans-serif;font-size:13px;display:flex;align-items:center;justify-content:center}
.ask-title{left:271px;top:892px;font-size:25px}
.crumb{left:271px;top:921px;font-size:7.5px;color:#888}
.crumb a{color:var(--blue)}
.faq{left:286px;top:933px;width:459px}
.faq li{list-style:none;height:31px;background:var(--row-bg);margin-bottom:4.5px;display:flex;align-items:center;justify-content:space-between;padding:0 10px 0 14px;font-family:"Yanone Kaffeesatz",sans-serif;color:var(--blue);font-size:13.5px}
.plus{width:18px;height:18px;border-radius:50%;background:var(--blue);position:relative}
.plus:before,.plus:after{content:"";position:absolute;background:#fff;left:4px;top:8px;width:10px;height:2px}
.plus:after{transform:rotate(90deg)}
.footer{left:0;top:1114px;width:792px;height:44px;background:var(--footer-bg);font-size:8px;color:#555}
.footer .copy{position:absolute;left:49px;top:20px}
.footer .links{position:absolute;left:522px;top:20px}
.footer a{color:#555}
</style>
</head>
<body>
<div class="page">
  <div class="abs brand"><span class="brand-mark"></span><span class="brand-name">Restwell Sleep Clinic</span></div>
  <div class="abs social"><span></span><span></span><span></span><span></span><span></span></div>
  <div class="abs contact-top">Call us: <a href="#">0-000-000-0000</a><br>Street, City, <a href="#">your@domain.com</a></div>
  <div class="abs search">Search</div>
  <div class="abs search-btn"><svg width="26" height="17" viewBox="0 0 26 17"><circle cx="12" cy="8" r="3" fill="none" stroke="#fff" stroke-width="1.5"/><line x1="14" y1="10" x2="16.5" y2="12.5" stroke="#fff" stroke-width="1.5"/></svg></div>
  <nav class="abs nav"><a href="#">HOME</a><a href="#">ABOUT US</a><a href="#">SERVICES</a><a href="#">OUR DOCTORS</a><a href="#">PRODUCTS</a><a href="#">CONTACT US</a></nav>

  <svg class="abs hero-deco" width="792" height="260" viewBox="0 0 792 260">
    <polygon points="0,60 49,80 49,120 0,100" fill="var(--red)"/>
    <polygon points="0,100 49,120 49,210 0,230" fill="#2f7fc7"/>
    <polygon points="745,90 792,130 792,210 745,180" fill="#cfcfcf"/>
    <polygon points="745,70 792,110 792,135 745,95" fill="var(--red)"/>
    <polygon points="770,200 792,180 792,232 750,232" fill="#2b9ad9"/>
  </svg>
  <div class="abs hero" role="img" aria-label="Bright blue abstract backdrop with light streaks">
    <div class="abs hero-photo" role="img" aria-label="Photo of a smiling doctor in a white coat with a stethoscope"></div>
  </div>
  <div class="abs hero-panel">
    <h1>SLEEP APNEA</h1>
    <p>Lid est laborum dolo rumes fugats untras. Et harums serrerum facilis dols nemis omnis fugiats vitaes nemo minimadips amets</p>
    <div class="more">READ DETAILS <i></i></div>
  </div>
  <div class="abs dots"><span></span><span></span><span></span><span></span></div>
  <div class="abs tab">LangSwitch</div>

  <h2 class="abs display intro">We are Restwell Sleep Clinic.</h2>
  <div class="abs cards">
    <div class="card"><div class="ico"><svg width="22" height="16" viewBox="0 0 22 16"><rect x="1" y="2" width="14" height="10" fill="none" stroke="#fff" stroke-width="1.5"/><path d="M15 5h4l2 4v3h-6z" fill="none" stroke="#fff" stroke-width="1.5"/><path d="M8 4v6M5 7h6" stroke="#fff" stroke-width="1.5"/><circle cx="5" cy="13" r="2" fill="#fff"/><circle cx="17" cy="13" r="2" fill="#fff"/></svg></div><h2>Emergency</h2><p>In convallis venenatis magna, nec interdum ipsum iaculis et. Nulla facilisi. Duis in neque malesuada vestibulum ut neque.</p></div>
    <div class="card"><div class="ico"><svg width="20" height="18" viewBox="0 0 20 18"><rect x="1" y="4" width="18" height="13" rx="2" fill="none" stroke="#fff" stroke-width="1.5"/><path d="M7 4V1h6v3M10 7v7M6.5 10.5h7" stroke="#fff" stroke-width="1.5" fill="none"/></svg></div><h2>Our Services</h2><p>In convallis venenatis magna, nec interdum ipsum iaculis et. Nulla facilisi. Duis in neque malesuada vestibulum ut neque.</p></div>
    <div class="card"><div class="ico"><svg width="20" height="20" viewBox="0 0 20 20"><path d="M3 2v6a4 4 0 0 0 8 0V2M7 12v3a3 3 0 0 0 6 0v-4" fill="none" stroke="#fff" stroke-width="1.5"/><circle cx="13" cy="9" r="2" fill="none" stroke="#fff" stroke-width="1.5"/></svg></div><h2>Share Information</h2><p>In convallis venenatis magna, nec interdum ipsum iaculis et. Nulla facilisi. Duis in neque malesuada vestibulum ut neque.</p></div>
    <div class="card"><div class="ico"><svg width="20" height="20" viewBox="0 0 20 20"><circle cx="10" cy="10" r="8" fill="none" stroke="#fff" stroke-width="1.5"/><path d="M2 10h16M10 2c-3 3-3 13 0 16M10 2c3 3 3 13 0 16" fill="none" stroke="#fff" stroke-width="1.2"/></svg></div><h2>Our Products</h2><p>In convallis venenatis magna, nec interdum ipsum iaculis et. Nulla facilisi. Duis in neque malesuada vestibulum ut neque.</p></div>
  </div>

  <h2 class="abs display doctors-title">Meet Our Doctors 1</h2>
  <div class="abs rule"></div>
  <div class="abs doctors">
    <div class="doc"><div role="img" aria-label="Portrait of a young male doctor" style="background:linear-gradient(135deg,#d9c2b0,#e9eef3)"></div></div>
    <div class="doc"><div role="img" aria-label="Female doctor with a patient" style="background:linear-gradient(135deg,#8a6a55,#dfe8ee)"></div></div>
    <div class="doc"><div role="img" aria-label="Portrait of a senior doctor with glasses" style="background:linear-gradient(135deg,#6b4d3c,#cfd6dc)"></div></div>
    <div class="doc"><div role="img" aria-label="Doctor with a stethoscope in a clinic" style="background:linear-gradient(135deg,#e4e8ec,#d9bba6 50%,#eef2f5)"></div></div>
  </div>

  <h2 class="abs display appt-title">Make an Appointment</h2>
  <div class="abs appt-rule"></div>
  <p class="abs appt-text">Our hospital open daily 07:00 - 20:00 for none dico emergency cases. Fusce dapibus, tellus ac cuisoe rsus commodo, tortor mauris condimen. Aenean ni lacinia bibendum nulla sed consectetur.</p>
  <div class="abs appt-line" style="top:1027px"><svg width="8" height="11" viewBox="0 0 8 11"><rect x=".5" y=".5" width="7" height="10" rx="1" fill="none" stroke="#555"/><rect x="2" y="2" width="4" height="4" fill="#555"/></svg>00-000-000-0000</div>
  <div class="abs appt-line" style="top:1049px"><svg width="11" height="8" viewBox="0 0 11 8"><rect x=".5" y=".5" width="10" height="7" fill="none" stroke="#555"/><path d="M.5 .5l5 4 5-4" fill="none" stroke="#555"/></svg><a href="#">your@domain.com</a></div>
  <div class="abs btn">Contact form</div>

  <h2 class="abs display ask-title">Ask a Question</h2>
  <div class="abs crumb"><a href="#">Home</a> / <a href="#">Ask a Question</a></div>
  <ul class="abs faq">
    <li>Proin libero risus, consequat quis congue ut, blandit id mauris.<span class="plus"></span></li>
    <li>Cras a massa mi, vel varius urna.tis nulla feugiat.<span class="plus"></span></li>
    <li>Vivamus nec odio et turpis mollis fringilla.<span class="plus"></span></li>
    <li>Duis egestas tincidunt erat, sit amet ultricies turpis interdum at.<span class="plus"></span></li>
    <li>Vivamus egestas aliquet quam eget volutpat. Fusce elementum tristique .<span class="plus"></span></li>
  </ul>

  <footer class="abs footer">
    <span class="copy">Copyright@2013-14 | Restwell Sleep clinic |</span>
    <span class="links"><a href="#">Home</a> | <a href="#">Contact</a> | <a href="#">Services</a> |</span>
  </footer>
</div>
</body>
</html>
```